Need a design for a pull up banner to promote a book

need a design for pull up banner (size 850mm x 2000mm) to promote a new book and the author. It has to be attractive design and grab attention.

I have attached the images of the book and some photos of the author.

my web address: https://dorivelkam.com

Business leaders

```html
<!DOCTYPE html>
<html lang="en">
<head>
<meta charset="utf-8">
<title>Dori Velkam – Pull-up Banner</title>
<link href="https://fonts.googleapis.com/css2?family=Montserrat:wght@400;500;600;800;900&display=swap" rel="stylesheet">
<style>
  :root {
    --stage: #6f706f;
    --brand-red: #d9163c;
    --deep-red: #7a0c22;
    --ink: #050505;
    --white: #ffffff;
  }
  * { margin: 0; padding: 0; box-sizing: border-box; }
  html, body {
    width: 1200px;
    height: 2167px;
    overflow: hidden;
    background: var(--stage);
  }
  .banner {
    position: absolute;
    left: 139px;
    top: 0;
    width: 921px;
    height: 2167px;
    overflow: hidden;
    background: linear-gradient(180deg,
      var(--brand-red) 0%,
      var(--brand-red) 24%,
      #b51133 40%,
      var(--deep-red) 55%,
      #2a040c 66%,
      var(--ink) 72%,
      var(--ink) 100%);
    font-family: "Montserrat", sans-serif;
  }
  .author-name {
    position: absolute;
    left: 0;
    top: 120px;
    width: 100%;
    text-align: center;
    color: var(--white);
    font-weight: 600;
    font-size: 104px;
    letter-spacing: 2px;
    line-height: 1;
  }
  .author-roles {
    position: absolute;
    left: 561px;
    top: 222px;
    color: var(--white);
    font-weight: 500;
    font-size: 15px;
    line-height: 24px;
    letter-spacing: 0.5px;
    text-transform: uppercase;
  }
  .author-photo {
    position: absolute;
    left: 51px;
    top: 465px;
    width: 828px;
    height: 1065px;
    border-radius: 260px 260px 0 0;
    background: radial-gradient(ellipse 60% 55% at 50% 45%,
      rgba(40, 20, 24, 0.55) 0%,
      rgba(30, 10, 14, 0.35) 55%,
      rgba(0, 0, 0, 0) 100%);
  }
  .book-mockup {
    position: absolute;
    left: 180px;
    top: 1005px;
    width: 540px;
    height: 485px;
    border-radius: 8px;
    background: linear-gradient(160deg, #e9e9ea 0%, #b9bcc4 45%, #2b3248 100%);
    opacity: 0.9;
  }
  .headline {
    position: absolute;
    left: 0;
    top: 1525px;
    width: 100%;
    text-align: center;
    font-weight: 900;
    text-transform: uppercase;
    line-height: 126px;
  }
  .headline span { display: block; }
  .headline .accent { color: var(--brand-red); font-size: 124px; }
  .headline .plain { color: var(--white); font-size: 124px; }
  .headline .wide { color: var(--white); font-size: 120px; letter-spacing: -1px; }
  .web-address {
    position: absolute;
    left: 0;
    top: 1972px;
    width: 100%;
    text-align: center;
    color: var(--white);
    font-weight: 400;
    font-size: 55px;
    line-height: 1.2;
  }
  .web-address strong { color: var(--brand-red); font-weight: 600; }
</style>
</head>
<body>
  <main class="banner">
    <div class="author-name">Dori Velkam</div>
    <div class="author-roles">Entrepreneur<br>Keynote Speaker<br>Author</div>

    <div class="author-photo" role="img" aria-label="Smiling author in glasses and a dark suit, holding out his book"></div>
    <div class="book-mockup" role="img" aria-label="The author's book shown as paperback, tablet and phone editions"></div>

    <h1 class="headline">
      <span class="accent">Unlock</span>
      <span class="plain">Your</span>
      <span class="wide">Potential</span>
    </h1>

    <p class="web-address">www.<strong>dorivelkam</strong>.com</p>
  </main>
</body>
</html>
```